Professional Business Cards

We need a nice looking, profession and modern business card for our new company. Our logo is attatched

Target Market(s)

Young Professionals

Industry/Entity Type

Financial

Contact Information for Business Card

FRONT

Morvane Tally Pty Ltd
Level 22, Halden Court, 48 Wirrapool St
Sydney NSW 2000
ABN : 57 304 918 226

Derek Wallis - Chief Operations Officer
P : 02 7153 2819
M: 0418 395 207
derek@morvanetally,com

BACK

- Cryptocurrency Exchange Services
- Cryptocurrency Mining Operations
- Cryptocurrency Investment Fund Offering

Font styles to use
Sans Serif

Colors
0255a3
9d9d9d

```html
<!DOCTYPE html>
<html lang="en">
<head>
<meta charset="utf-8">
<title>Morvane Tally Business Cards</title>
<link rel="stylesheet" href="https://fonts.googleapis.com/css2?family=Source+Sans+3:wght@400;600;700&display=swap">
<style>
  :root {
    --brand-blue: #0255a3;
    --brand-blue-light: #1a7fd6;
    --brand-grey: #9d9d9d;
    --text-dark: #3a3a3a;
    --text-mid: #5e5e5e;
    --paper: #ffffff;
    --backdrop: #e4e5e7;
  }
  * { box-sizing: border-box; margin: 0; padding: 0; }
  html, body {
    width: 1200px; height: 840px; overflow: hidden;
    background: var(--backdrop);
    font-family: "Source Sans 3", "Helvetica Neue", Arial, sans-serif;
  }
  .canvas { position: relative; width: 1200px; height: 840px; }
  .card {
    position: absolute; width: 600px; height: 343px;
    border-radius: 3px; overflow: hidden;
    box-shadow: 0 12px 28px rgba(0,0,0,0.22);
  }

  /* Back side */
  .card-back {
    left: 110px; top: 60px;
    background: linear-gradient(135deg, var(--brand-blue-light) 0%, var(--brand-blue) 60%, #01468a 100%);
    color: var(--paper);
  }
  .card-back .brand {
    position: absolute; left: 0; right: 0; top: 118px;
    display: flex; justify-content: center; align-items: center; gap: 18px;
  }
  .brand-square { width: 48px; height: 48px; background: currentColor; }
  .brand-name {
    font-weight: 700; font-size: 50px; letter-spacing: 1px; line-height: 1;
  }
  .services {
    position: absolute; left: 0; right: 0; bottom: 42px;
    text-align: center; font-size: 15px; line-height: 1.35; font-weight: 400;
  }

  /* Front side */
  .card-front {
    left: 490px; top: 430px;
    background: var(--paper); color: var(--text-dark);
  }
  .card-front .brand {
    position: absolute; left: 176px; top: 40px;
    display: flex; align-items: center; gap: 12px; color: var(--brand-blue);
  }
  .card-front .brand-square { width: 32px; height: 32px; background: var(--brand-grey); }
  .card-front .brand-name { font-size: 34px; }
  .brand-rule {
    position: absolute; left: 176px; right: 50px; top: 100px;
    height: 1px; background: var(--brand-grey);
  }
  .company {
    position: absolute; right: 50px; top: 116px; text-align: right;
    font-size: 14px; line-height: 1.3; color: var(--text-mid);
  }
  .company .company-name { font-weight: 700; color: var(--text-dark); }
  .person { position: absolute; left: 36px; top: 182px; }
  .person-name { font-size: 20px; font-weight: 700; color: var(--brand-blue); letter-spacing: 0.3px; }
  .person-title { font-size: 14px; color: var(--text-mid); margin-top: -2px; }
  .person-rule {
    position: absolute; left: 36px; top: 232px; width: 300px;
    height: 1px; background: var(--brand-grey);
  }
  .contacts {
    position: absolute; left: 36px; top: 240px;
    list-style: none; font-size: 14px; line-height: 18px; color: var(--text-mid);
  }
  .contacts li { display: flex; align-items: center; gap: 7px; }
  .contacts svg { width: 12px; height: 12px; fill: var(--brand-blue); flex: none; }
  .contacts .abn { margin-top: 3px; padding-left: 0; }
  .footer-band {
    position: absolute; left: 0; right: 0; bottom: 0; height: 14px;
    background: var(--brand-blue);
    border-top: 4px solid #d8d8d8;
  }
</style>
</head>
<body>
<main class="canvas">

  <section class="card card-back" aria-label="Card back">
    <div class="brand">
      <span class="brand-square"></span>
      <span class="brand-name">Morvane Tally</span>
    </div>
    <p class="services">
      Cryptocurrency Exchange Services &bull; Cryptocurrency Mining Operations<br>
      Cryptocurrency Investment Fund Offering
    </p>
  </section>

  <section class="card card-front" aria-label="Card front">
    <div class="brand">
      <span class="brand-square"></span>
      <span class="brand-name">Morvane Tally</span>
    </div>
    <div class="brand-rule"></div>

    <address class="company" style="font-style:normal">
      <div class="company-name">Morvane Tally Pty Ltd</div>
      <div>Level 22, Halden Court, 48</div>
      <div>Wirrapool St, Sydney NSW 2000</div>
    </address>

    <div class="person">
      <div class="person-name">DEREK WALLIS</div>
      <div class="person-title">Chief Operations Officer</div>
    </div>
    <div class="person-rule"></div>

    <ul class="contacts">
      <li>
        <svg viewBox="0 0 24 24" aria-hidden="true"><path d="M6.6 10.8a15.1 15.1 0 0 0 6.6 6.6l2.2-2.2c.3-.3.7-.4 1-.2 1.1.4 2.3.6 3.6.6.6 0 1 .4 1 1V20c0 .6-.4 1-1 1A17 17 0 0 1 3 4c0-.6.4-1 1-1h3.5c.6 0 1 .4 1 1 0 1.3.2 2.5.6 3.6.1.3 0 .7-.2 1z"/></svg>
        02 7153 2819
      </li>
      <li>
        <svg viewBox="0 0 24 24" aria-hidden="true"><path d="M7 1h10a2 2 0 0 1 2 2v18a2 2 0 0 1-2 2H7a2 2 0 0 1-2-2V3a2 2 0 0 1 2-2zm0 3v14h10V4zm5 15.5a1 1 0 1 0 0 2 1 1 0 0 0 0-2z"/></svg>
        0418 395 207
      </li>
      <li>
        <svg viewBox="0 0 24 24" aria-hidden="true"><path d="M2 5h20v14H2zm2 2v.5l8 5 8-5V7zm0 2.8V17h16V9.8l-8 5z"/></svg>
        derek@morvanetally,com
      </li>
      <li class="abn">ABN : 57 304 918 226</li>
    </ul>

    <div class="footer-band"></div>
  </section>

</main>
</body>
</html>
```